Social Media designs (LinkedIn banner, LinkedIn posts, Instagram)

Hello designers!
We are looking to create some more concepts for our social media identity for a search firm (recruitment company)
I have attached a "brand toolkit" that shows our brand, logo, colour scheme to guide you with regards to colours and identiy.

You will see in the brand toolkit there are some examples of;
- A LinkedIn banner for the company (page 23)
- Social Media posts for LinkedIn and Instagram (page 21)

What we are looking for...

We don't really like the current LinkedIn banner ideas. We would like to see more concepts that look more aesthetically pleasing - the current ideas look quite dull.

We DO like the social media post concepts but we would like to have more templates/options that we can use (similar themes)

We welcome submissions for Social Media designs that we can use with our company branding. Thank you for your work in advance!

```html
<!DOCTYPE html>
<html lang="en">
<head>
<meta charset="utf-8">
<title>Talent knows no borders – social set</title>
<link href="https://fonts.googleapis.com/css2?family=Figtree:wght@500&display=swap" rel="stylesheet">
<style>
  :root {
    --canvas: #ffffff;
    --ink-dark: #15241f;
    --forest: #17382c;
    --sea-deep: #1f5a47;
    --sea: #3a9e84;
    --sea-light: #5cc2a5;
    --cream: #e7e4da;
    --frame: #ffffff;
  }
  * { box-sizing: border-box; margin: 0; padding: 0; }
  html, body {
    width: 1200px; height: 1200px; overflow: hidden;
    background: var(--canvas);
    font-family: "Figtree", "Helvetica Neue", Arial, sans-serif;
  }
  .canvas { position: relative; width: 1200px; height: 1200px; }

  /* LinkedIn banner */
  .banner {
    position: absolute; left: 36px; top: 64px; width: 1128px; height: 191px;
    overflow: hidden;
  }
  .banner__photo {
    position: absolute; inset: 0;
    background: linear-gradient(90deg, var(--forest) 0%, var(--sea-deep) 55%, var(--sea) 70%, var(--sea-light) 85%, var(--sea) 100%);
  }
  .banner__headline {
    position: absolute; right: 334px; top: 22px;
    text-align: right; color: var(--cream);
    font-weight: 500; font-size: 54px; line-height: 72px; letter-spacing: 0.2px;
  }

  /* Brand tile */
  .brand-tile {
    position: absolute; left: 100px; top: 134px; width: 201px; height: 201px;
    background: var(--ink-dark);
    border: 5px solid var(--frame);
    box-shadow: 0 10px 24px rgba(0,0,0,0.22);
    display: flex; align-items: center; justify-content: center;
  }
  .brand-tile__name {
    color: var(--cream); font-weight: 500; font-size: 40px;
  }

  /* Square post */
  .post {
    position: absolute; left: 258px; top: 298px; width: 864px; height: 864px;
    overflow: hidden;
  }
  .post__photo {
    position: absolute; inset: 0;
    background:
      radial-gradient(circle at 75% 25%, var(--sea-light) 0%, var(--sea) 30%, transparent 60%),
      linear-gradient(90deg, var(--forest) 0%, var(--sea-deep) 35%, var(--sea) 75%, var(--sea-deep) 100%);
  }
  .post__panel {
    position: absolute; left: 34px; top: 277px; width: 561px; height: 558px;
    background: var(--ink-dark);
  }
  .post__headline {
    position: absolute; left: 44px; top: 128px;
    color: var(--cream); font-weight: 500; font-size: 102px; line-height: 130px;
    letter-spacing: 0.5px;
  }
</style>
</head>
<body>
<main class="canvas">
  <section class="banner">
    <div class="banner__photo" role="img" aria-label="Aerial photograph of a surfer lying on a coral surfboard in turquoise ocean water, fading into dark green on the left"></div>
    <h2 class="banner__headline">Talent knows<br>no borders</h2>
  </section>

  <section class="post">
    <div class="post__photo" role="img" aria-label="Aerial photograph of a surfer lying on a coral surfboard in foamy turquoise sea water, darkening towards the left"></div>
    <div class="post__panel">
      <h1 class="post__headline">Talent<br>knows no<br>borders</h1>
    </div>
  </section>

  <div class="brand-tile">
    <span class="brand-tile__name">Kestrel</span>
  </div>
</main>
</body>
</html>
```